Fashion clothing business needs a label, swing tag and business card.

Independent womenswear label called "Tessa Wrenly".
I'd like a design for a woven label to go on the clothes, a swing tag and business card design. The design should be simple, modern but timeless. Its a small business, made locally in Melbourne, Australia, produces quality garments for everyday wear using beautiful fabrics.

Reason: just waiting for a few others to submit their designs.

Target Market(s)

30+ ladies, who want quality everyday wear, who don't necessarily follow trends. They can be a bit edgy and willing to take a risk with something different.

Industry/Entity Type

Clothing

Font styles to use
Other font styles liked:
• I dont mind the typewriter font, but can it look modern? happy for you to choose.

Requirements
Should not have
• A difficult shape swing tag - as it might be more expensive for me to get printed and cut.

```html
<!DOCTYPE html>
<html lang="en">
<head>
<meta charset="utf-8">
<title>Tessa Wrenly – Label, Swing Tag and Business Card</title>
<link rel="stylesheet" href="https://fonts.googleapis.com/css2?family=Courier+Prime:wght@700&family=Cormorant+Garamond:wght@600;700&display=swap">
<style>
  :root {
    --olive: #44591f;
    --cream: #ede7c7;
    --ink: #111111;
    --paper: #ffffff;
    --type-serif: "Cormorant Garamond", Georgia, serif;
    --type-contact: "Courier Prime", "Courier New", monospace;
  }
  * { box-sizing: border-box; margin: 0; padding: 0; }
  html, body { width: 1200px; height: 800px; overflow: hidden; background: var(--paper); }
  .sheet { position: relative; width: 1200px; height: 800px; background: var(--paper); }

  .piece { position: absolute; }
  .frame { position: absolute; }

  .brand-name {
    font-family: var(--type-serif);
    font-weight: 600;
    line-height: 1;
    white-space: nowrap;
  }
  .origin {
    font-family: var(--type-serif);
    font-weight: 700;
    text-transform: uppercase;
    letter-spacing: 1.5px;
    line-height: 1;
    white-space: nowrap;
  }

  /* Woven labels */
  .woven-label {
    width: 360px; height: 200px;
    border: 10px solid var(--olive);
    display: flex; flex-direction: column; align-items: center; justify-content: center;
    gap: 10px;
    background: var(--paper);
  }
  .woven-label--olive { left: 60px; top: 44px; color: var(--olive); }
  .woven-label--mono { left: 66px; top: 290px; color: var(--ink); border-color: var(--ink); }
  .woven-label .brand-name { font-size: 50px; }
  .woven-label .origin { font-size: 14px; }

  /* Business card */
  .business-card {
    left: 466px; top: 64px; width: 694px; height: 396px;
    background: var(--olive);
  }
  .business-card__name-frame {
    left: 20px; top: 16px; width: 658px; height: 186px;
    border: 5px solid var(--cream);
    display: flex; align-items: center; justify-content: center;
  }
  .business-card .brand-name { color: var(--cream); font-size: 92px; }
  .business-card__contact {
    left: 20px; top: 226px; width: 658px; height: 154px;
    background: var(--cream);
    padding: 34px 0 0 84px;
    font-family: var(--type-contact);
    font-weight: 700;
    font-size: 25px;
    letter-spacing: 2px;
    color: var(--olive);
    line-height: 42px;
  }

  /* Swing tag */
  .swing-tag {
    top: 534px; height: 230px;
    background: var(--cream);
    color: var(--olive);
  }
  .swing-tag--front { left: 136px; width: 460px; }
  .swing-tag--back { left: 634px; width: 462px; }
  .swing-tag__frame {
    left: 28px; top: 20px; right: 18px; bottom: 16px;
    border: 5px solid var(--olive);
  }
  .swing-tag--front .brand-name {
    position: absolute; left: 0; right: 0; top: 58px;
    text-align: center; font-size: 58px;
  }
  .swing-tag--front .origin {
    position: absolute; left: 0; right: 0; top: 124px;
    text-align: center; font-size: 15px;
  }
  .swing-tag__email {
    position: absolute; right: 14px; bottom: 10px;
    font-family: var(--type-contact); font-weight: 700;
    font-size: 14px; letter-spacing: 0.5px;
  }
  .tag-field {
    position: absolute; left: 0; width: 100%; height: 30px;
  }
  .tag-field__label {
    position: absolute; right: calc(100% - 110px); bottom: 2px;
    font-family: var(--type-serif); font-weight: 700; font-size: 15px;
    text-transform: uppercase; letter-spacing: 0.5px; white-space: nowrap;
  }
  .tag-field__line {
    position: absolute; left: 118px; width: 266px; bottom: 4px;
    border-bottom: 2px solid var(--olive);
  }
  .tag-field--size { top: 34px; }
  .tag-field--style { top: 84px; }
  .tag-field--price { top: 134px; }
</style>
</head>
<body>
<main class="sheet">

  <section class="piece woven-label woven-label--olive" aria-label="Woven label, olive">
    <span class="brand-name">Tessa Wrenly</span>
    <span class="origin">Made in Australia</span>
  </section>

  <section class="piece woven-label woven-label--mono" aria-label="Woven label, black">
    <span class="brand-name">Tessa Wrenly</span>
    <span class="origin">Made in Australia</span>
  </section>

  <section class="piece business-card" aria-label="Business card">
    <div class="frame business-card__name-frame">
      <span class="brand-name">Tessa Wrenly</span>
    </div>
    <div class="frame business-card__contact">
      <p>e-mail: info@tessawrenly.com</p>
      <p>mobile: 0400318625</p>
    </div>
  </section>

  <section class="piece swing-tag swing-tag--front" aria-label="Swing tag, front">
    <div class="frame swing-tag__frame">
      <span class="brand-name">Tessa Wrenly</span>
      <span class="origin">Made in Australia</span>
      <span class="swing-tag__email">info@tessawrenly.com</span>
    </div>
  </section>

  <section class="piece swing-tag swing-tag--back" aria-label="Swing tag, back">
    <div class="frame swing-tag__frame">
      <div class="tag-field tag-field--size"><span class="tag-field__label">Size:</span><span class="tag-field__line"></span></div>
      <div class="tag-field tag-field--style"><span class="tag-field__label">Style:</span><span class="tag-field__line"></span></div>
      <div class="tag-field tag-field--price"><span class="tag-field__label">Price:</span><span class="tag-field__line"></span></div>
    </div>
  </section>

</main>
</body>
</html>
```